Medical Supply company in need of mail flyers

We are a medical supply company based out of West Palm Beach, Florida. Our website is StrideFreeSteps.Com but we also go by Harborlight Medical Supply. We provide shoes through various insurance companies at no cost to the client.We're in need of multiple mail flyers for diabetic footwear customer retention. We will be choosing the top 2 designs submitted.

Industry/Entity Type

Medical Equipment

Requirements
Must have
• Flyers must be 6x9

```html
<!DOCTYPE html>
<html lang="en">
<head>
<meta charset="utf-8">
<title>Diabetic Footwear – 4 Easy Steps</title>
<link href="https://fonts.googleapis.com/css2?family=Poppins:ital,wght@0,600;0,700;1,700&family=Arimo:wght@700&display=swap" rel="stylesheet">
<style>
  :root {
    --green: #7dc96e;
    --blue: #4a78a0;
    --white: #ffffff;
    --ink: #111111;
  }
  * { margin: 0; padding: 0; box-sizing: border-box; }
  html, body { width: 800px; height: 1200px; overflow: hidden; background: var(--white); }
  .flyer { position: relative; width: 800px; height: 1200px; overflow: hidden; background: var(--white); }

  .title-band-green { position: absolute; left: 60px; top: 74px; width: 740px; height: 98px; background: var(--green); }
  .title-diabetic {
    position: absolute; left: 78px; top: 70px;
    font-family: "Poppins", sans-serif; font-weight: 700; font-size: 84px;
    letter-spacing: -4px; color: var(--white); line-height: 1;
  }
  .title-band-blue { position: absolute; left: 0; top: 174px; width: 650px; height: 100px; }
  .title-footwear {
    position: absolute; left: 180px; top: 180px;
    font-family: "Poppins", sans-serif; font-weight: 700; font-style: italic; font-size: 80px;
    letter-spacing: -4px; color: var(--white); line-height: 1;
  }

  .shoe-gallery { position: absolute; left: 0; top: 296px; width: 800px; height: 414px; }
  .shoe-photo { position: absolute; top: 0; height: 414px; }
  .shoe-photo.sneaker { left: 0; width: 246px; background: linear-gradient(135deg, #6f6a68, #514c4b 55%, #7b8592); }
  .shoe-photo.mary-jane { left: 248px; width: 300px; background: linear-gradient(160deg, #5a3d28, #8a5a34 50%, #4b3220); }
  .shoe-photo.walker { left: 550px; width: 250px; background: linear-gradient(145deg, #9fb3c4, #7f95a8 55%, #a9b9c6); }

  .step-count {
    position: absolute; left: 0; width: 800px; top: 612px; text-align: center;
    font-family: "Arimo", sans-serif; font-weight: 700; font-size: 250px;
    color: var(--blue); line-height: 1;
  }
  .steps-band {
    position: absolute; left: 62px; top: 830px; width: 674px; height: 76px;
    background: var(--blue); color: var(--white); text-align: center;
    font-family: "Arimo", sans-serif; font-weight: 700; font-size: 58px; line-height: 76px;
    letter-spacing: 1px;
  }
  .steps-line {
    position: absolute; left: 0; width: 800px; text-align: center;
    font-family: "Arimo", sans-serif; font-weight: 700; font-size: 42px; line-height: 1;
    transform: scaleX(0.9);
  }
  .steps-line.receive { top: 900px; color: var(--blue); }
  .steps-line.shoes { top: 940px; color: var(--green); }
  .login-tag {
    position: absolute; left: 314px; top: 978px; width: 171px; height: 36px;
    background: var(--green); color: var(--white); text-align: center;
    font-family: "Arimo", sans-serif; font-weight: 700; font-size: 28px; line-height: 36px;
  }
  .web-address {
    position: absolute; left: 0; width: 800px; top: 1016px; text-align: center;
    font-family: "Arimo", sans-serif; font-weight: 700; font-size: 28px; color: var(--green);
  }

  .brand-name {
    position: absolute; top: 1098px;
    font-family: "Arimo", sans-serif; font-weight: 700; font-size: 30px; line-height: 1;
    display: flex; align-items: center; gap: 10px;
  }
  .brand-name.supply { left: 70px; color: var(--ink); }
  .brand-name.shoes-site { left: 480px; color: var(--blue); }
  .brand-mark { width: 26px; height: 26px; border-radius: 50%; background: var(--ink); }
  .brand-mark.square { border-radius: 0; background: var(--blue); }
</style>
</head>
<body>
<main class="flyer">
  <div class="title-band-green"></div>
  <h1 class="title-diabetic">Diabetic</h1>
  <svg class="title-band-blue" viewBox="0 0 650 100" aria-hidden="true">
    <polygon points="0,0 644,0 580,100 0,100" fill="#4a78a0"/>
  </svg>
  <h2 class="title-footwear">Footwear</h2>

  <section class="shoe-gallery">
    <div class="shoe-photo sneaker" role="img" aria-label="Grey and orange diabetic sneakers on slate tiles"></div>
    <div class="shoe-photo mary-jane" role="img" aria-label="Tan leather strap shoes on a wooden floor"></div>
    <div class="shoe-photo walker" role="img" aria-label="Black walking shoes on blue stone"></div>
  </section>

  <div class="step-count">4</div>
  <div class="steps-band">EASY STEPS</div>
  <p class="steps-line receive">TO RECEIVE YOUR NEW</p>
  <p class="steps-line shoes">THERAPEUTIC SHOES.</p>
  <div class="login-tag">LOGIN TO</div>
  <p class="web-address">StrideFreeSteps.Com</p>

  <div class="brand-name supply"><span class="brand-mark"></span>Harborlight Medical</div>
  <div class="brand-name shoes-site">StrideFree Steps<span class="brand-mark square"></span></div>
</main>
</body>
</html>
```